Brambleton Chiropractic. We have two locations that we want to advertise on the same card. Kelwin MotionCare campus address: 3815 Tamsey Rd., Suite 240, Flowood, MS 39987. Madison address: 428 Pellham Ct., Building D., Madison, MS 39974. website: www.drbrambleton-example.com. o:(601)555-0147 f:(601)555-0183

Target Market(s)

Health care decision makers: primary care doctors and mothers

Contact Information for Business Card

I have no idea; up for any suggestions and I'd do much better picking from examples versus describing what I'm looking for. We are in a very high end location and would like the cards to look really sharp.

Requirements
Must have
• My name, Marcus L Denbrook, D.C.

```html
<!DOCTYPE html>
<html lang="en">
<head>
<meta charset="utf-8">
<title>Brambleton Chiropractic – Business Card</title>
<link href="https://fonts.googleapis.com/css2?family=Cinzel:wght@500&family=Cormorant+Garamond:ital,wght@1,500&family=Roboto:wght@400;500&display=swap" rel="stylesheet">
<style>
  :root {
    --page: #e4e4e4;
    --card-dark: #2b2b2b;
    --card-light: #ffffff;
    --ink-light: #f2f2f2;
    --ink-dark: #1c1c1c;
    --ink-muted: #3a3a3a;
    --rule: #2a2a2a;
  }
  * { margin: 0; padding: 0; box-sizing: border-box; }
  html, body { width: 1200px; height: 930px; overflow: hidden; background: var(--page); }
  .canvas { position: relative; width: 1200px; height: 930px; }

  .card {
    position: absolute;
    width: 560px; height: 320px;
    border-radius: 16px;
    box-shadow: 0 8px 24px rgba(0,0,0,0.18);
    overflow: hidden;
  }
  .card--front { left: 90px; top: 110px; background: var(--card-dark); color: var(--ink-light); }
  .card--back  { left: 550px; top: 490px; background: var(--card-light); color: var(--ink-dark); }

  .brand { position: absolute; }
  .brand__name {
    font-family: "Cinzel", serif; font-weight: 500;
    text-transform: uppercase; letter-spacing: 1px; line-height: 1;
  }
  .brand__campus { font-family: "Cormorant Garamond", serif; font-style: italic; font-weight: 500; }
  .brand__address { font-family: "Cinzel", serif; text-transform: uppercase; letter-spacing: .5px; }

  .card--front .brand { left: 150px; top: 118px; }
  .card--front .brand__name { font-size: 27px; }
  .card--front .brand__campus { font-size: 17px; margin-top: 8px; }
  .card--front .brand__address { font-size: 7.5px; margin-top: 4px; }

  .card--back .brand { right: 34px; top: 40px; text-align: left; }
  .card--back .brand__name { font-size: 21px; }
  .card--back .brand__campus { font-size: 13px; margin-top: 6px; }
  .card--back .brand__address { font-size: 6px; margin-top: 3px; }

  .rule { position: absolute; height: 1.5px; background: var(--rule); }
  .rule--top { left: 34px; right: 34px; top: 138px; }
  .rule--mid { left: 34px; width: 250px; top: 236px; }

  .person { position: absolute; left: 34px; top: 178px; font-family: "Roboto", sans-serif; }
  .person__name { font-size: 17px; font-weight: 500; text-transform: uppercase; letter-spacing: .3px; }
  .person__role { font-size: 14px; color: var(--ink-muted); margin-top: 3px; }

  .location { position: absolute; right: 34px; top: 160px; text-align: right; font-family: "Roboto", sans-serif; font-size: 14px; line-height: 1.4; }

  .contacts { position: absolute; left: 34px; top: 248px; list-style: none; font-family: "Roboto", sans-serif; font-size: 15px; line-height: 21px; }
  .contacts li { display: flex; align-items: center; gap: 9px; }
  .contacts svg { width: 12px; height: 12px; fill: var(--ink-muted); }
</style>
</head>
<body>
<main class="canvas">

  <section class="card card--front" aria-label="Card front">
    <div class="brand">
      <p class="brand__name">Brambleton Chiropractic</p>
      <p class="brand__campus">Kelwin MotionCare Campus</p>
      <p class="brand__address">3815 Tamsey Rd., Suite 240 &nbsp;Flowood, MS 39987</p>
    </div>
  </section>

  <section class="card card--back" aria-label="Card back">
    <div class="brand">
      <p class="brand__name">Brambleton Chiropractic</p>
      <p class="brand__campus">Kelwin MotionCare Campus</p>
      <p class="brand__address">3815 Tamsey Rd., Suite 240 &nbsp;Flowood, MS 39987</p>
    </div>
    <div class="rule rule--top"></div>

    <div class="person">
      <p class="person__name">Marcus L Denbrook, D.C.</p>
      <p class="person__role">Director</p>
    </div>

    <address class="location" style="font-style:normal">
      428 Pellham Ct., Building D.,<br>Madison, MS 39974.
    </address>

    <div class="rule rule--mid"></div>

    <ul class="contacts">
      <li>
        <svg viewBox="0 0 24 24" aria-hidden="true"><path d="M6.6 10.8a15.1 15.1 0 0 0 6.6 6.6l2.2-2.2a1 1 0 0 1 1-.25 11.4 11.4 0 0 0 3.6.57 1 1 0 0 1 1 1V20a1 1 0 0 1-1 1A17 17 0 0 1 3 4a1 1 0 0 1 1-1h3.5a1 1 0 0 1 1 1c0 1.25.2 2.45.57 3.57a1 1 0 0 1-.25 1z"/></svg>
        (601)555-0147
      </li>
      <li>
        <svg viewBox="0 0 24 24" aria-hidden="true"><path d="M6 2h12v5H6zM4 8h16a2 2 0 0 1 2 2v6h-4v6H6v-6H2v-6a2 2 0 0 1 2-2zm4 8v4h8v-4z"/></svg>
        (601)555-0183
      </li>
      <li>
        <svg viewBox="0 0 24 24" aria-hidden="true"><path d="M12 2a10 10 0 1 0 0 20 10 10 0 0 0 0-20zm6.9 6h-3a15.6 15.6 0 0 0-1.3-3.6A8 8 0 0 1 18.9 8zM12 4c.8 1.2 1.5 2.5 1.9 4h-3.8c.4-1.5 1.1-2.8 1.9-4zM4.3 14a8 8 0 0 1 0-4h3.4a16.5 16.5 0 0 0 0 4zm.8 2h3a15.6 15.6 0 0 0 1.3 3.6A8 8 0 0 1 5.1 16zm3-8h-3a8 8 0 0 1 4.3-3.6A15.6 15.6 0 0 0 8.1 8zM12 20c-.8-1.2-1.5-2.5-1.9-4h3.8c-.4 1.5-1.1 2.8-1.9 4zm2.3-6H9.7a14.7 14.7 0 0 1 0-4h4.6a14.7 14.7 0 0 1 0 4zm.3 5.6a15.6 15.6 0 0 0 1.3-3.6h3a8 8 0 0 1-4.3 3.6zm1.7-5.6a16.5 16.5 0 0 0 0-4h3.4a8 8 0 0 1 0 4z"/></svg>
        www.drbrambleton-example.com
      </li>
    </ul>
  </section>

</main>
</body>
</html>
```